Classic, clean, and fun community pool party door hangers

Looking for a classy, but FUn door hangers for a community outreach pool party.
While we are a faith-based organization, we do NOT want this to look religious.
RGB Color # 4c7991
Template included

Target Market(s)

Families

Font styles to use
Sans Serif

Colors
f37122
959595
dbdbdb

Requirements
Must have
• Date: July 26, 2018 Thursday
• Time: 5:30pm - 7:30pm MDT
• Location: Harrowgate Pool: 2840 9th Ave NW, Maplecrest, CO 80412
• Free food while it lasts, games, prizes, swimming, and raffle
Should not have
• No Religious symbols

```html
<!DOCTYPE html>
<html lang="en">
<head>
<meta charset="utf-8">
<title>Community Pool Party Door Hanger</title>
<link rel="stylesheet" href="https://fonts.googleapis.com/css2?family=Rubik:wght@400;500;700&display=swap">
<style>
  :root {
    --orange: #f37122;
    --grey-mid: #959595;
    --grey-light: #dbdbdb;
    --ink: #1c1c1c;
    --paper: #ffffff;
    --backdrop: #ececec;
    --address: #4a4a4a;
  }
  html, body {
    margin: 0;
    width: 1200px;
    height: 869px;
    overflow: hidden;
    background: var(--backdrop);
  }
  .stage {
    width: 1200px;
    height: 869px;
    display: flex;
    align-items: center;
    justify-content: center;
  }
  .door-hanger { width: 320px; height: 792px; display: block; }
  .paper { fill: var(--paper); }
  .hole { fill: var(--backdrop); }
  .slot { stroke: var(--backdrop); stroke-width: 6; stroke-linecap: round; }
  .star-light { fill: var(--grey-light); }
  .star-mid { fill: var(--grey-mid); }
  .star-ink { fill: var(--ink); }
  .star-orange { fill: var(--orange); }
  .ring { fill: none; stroke: var(--orange); stroke-width: 26; }
  .ring-inner { fill: var(--paper); }
  .ring-title {
    font-family: "Rubik", sans-serif; font-weight: 700; font-size: 16px;
    fill: var(--paper); letter-spacing: 0.4px;
  }
  .month {
    font-family: "Rubik", sans-serif; font-weight: 700; font-size: 19px;
    fill: var(--ink); text-anchor: middle;
  }
  .day {
    font-family: "Rubik", sans-serif; font-weight: 500; font-size: 72px;
    fill: var(--orange); text-anchor: middle;
  }
  .year {
    font-family: "Rubik", sans-serif; font-weight: 400; font-size: 11px;
    fill: var(--ink); text-anchor: middle;
  }
  .perks {
    font-family: "Rubik", sans-serif; font-weight: 700; font-size: 12px;
    fill: var(--orange); text-anchor: middle;
  }
  .hashtag {
    font-family: "Rubik", sans-serif; font-weight: 400; font-size: 24px;
    fill: var(--ink); text-anchor: middle;
  }
  .time-band { fill: var(--orange); }
  .time {
    font-family: "Rubik", sans-serif; font-weight: 500; font-size: 12px;
    fill: var(--paper); text-anchor: middle;
  }
  .address {
    font-family: "Rubik", sans-serif; font-weight: 400; font-size: 9.5px;
    fill: var(--address); text-anchor: middle;
  }
</style>
</head>
<body>
<main class="stage">
  <svg class="door-hanger" viewBox="0 0 210 520" role="img" aria-label="Community Pool Party door hanger">
    <defs>
      <path id="star" d="M0,-1 L.223,-.307 L.951,-.309 L.361,.117 L.588,.809 L0,.38 L-.588,.809 L-.361,.117 L-.951,-.309 L-.223,-.307 Z"/>
      <clipPath id="hanger-edge"><rect width="210" height="520"/></clipPath>
      <path id="title-arc" d="M32.8,259.4 A80,80 0 1 1 187.7,239"/>
    </defs>

    <rect class="paper" width="210" height="520"/>

    <g class="decor-stars" clip-path="url(#hanger-edge)">
      <use href="#star" class="star-light" transform="translate(28,40) scale(48)"/>
      <use href="#star" class="star-mid" transform="translate(190,110) scale(90) rotate(8)"/>
      <use href="#star" class="star-ink" transform="translate(163,31) scale(16)"/>
      <use href="#star" class="star-ink" transform="translate(38,120) scale(22)"/>
      <use href="#star" class="star-light" transform="translate(32,290) scale(22)"/>
      <use href="#star" class="star-mid" transform="translate(180,292) scale(36)"/>
      <use href="#star" class="star-orange" transform="translate(30,350) scale(11)"/>
      <use href="#star" class="star-ink" transform="translate(183,353) scale(11)"/>
    </g>

    <g class="hanger-cut">
      <line class="slot" x1="55" y1="0" x2="90" y2="36"/>
      <circle class="hole" cx="107" cy="69" r="46"/>
    </g>

    <g class="date-badge">
      <circle class="ring-inner" cx="108" cy="232" r="73"/>
      <circle class="ring" cx="108" cy="232" r="86"/>
      <text class="ring-title"><textPath href="#title-arc" startOffset="50%" text-anchor="middle">COMMUNITY POOL PARTY</textPath></text>
      <text class="month" x="107" y="188">JULY</text>
      <text class="day" x="107" y="254">26</text>
      <text class="year" x="107" y="280">2018 Thursday</text>
    </g>

    <text class="perks">
      <tspan x="107" y="340">Free food while it lasts,</tspan>
      <tspan x="107" y="356">games, prizes,</tspan>
      <tspan x="107" y="372">swimming, and raffle</tspan>
    </text>

    <text class="hashtag" x="105" y="420">#ForMaplecrest</text>

    <rect class="time-band" x="0" y="449" width="210" height="21"/>
    <text class="time" x="105" y="463.5">5:30pm - 7:30pm MDT</text>

    <text class="address">
      <tspan x="105" y="487">Harrowgate Pool: 2840 9th Ave NW,</tspan>
      <tspan x="105" y="502">Maplecrest, CO 80412</tspan>
    </text>
  </svg>
</main>
</body>
</html>
```